Luxury Eye Cream Label

Velo Skina is developing a line of luxury dermatology creams designed to improve and treat various skin conditions and esthetic problems.
All creams are handmade by registered pharmacies according to patient needs, on the same day of the order. (meaning the creams are not premade. the creams are freshly made without any preservatives or stabilizers.)
The labels are two. One for the upper lid of an aluminum container 4.0 cm. in diameter containing company logo and description of the cream. The other one is for the bottom of the container 4.0 in diameter containing pharmacy information.
The label should convey professional, MD, and luxury feel.
(Upper Lid Label)
Logo of velo skina
EYE CARE CREAM - intensive
Doctor Series
handmade . Doctor formulated . registered Pharmacy . highest ethical standards . (in a circular pattern on the label)
Ingredients: Marigold extract, Witch Hazel Distillate, Water, Glycerin, Stearyl Alcohol, Wheat Germ Oil, Polysorbate 60, Sesame Oil, Myristyl Myristate, Cetyl Alcohol, Sorbitan Stearate, Phenoxyethanol, Calendula Extract, Cornflower Extract, Sodium Alginate, Sodium Citrate, Mica, Vit. C, Vit. E.
Please, adhere to the above content, and dimension of the label of 4 cm in diameter. Also, please view it to scale. This is a relatively small container, aluminum ½ ounce (15ml) cream.
The Bottom of the Jar will have a label with the following information. This is obligatory, because of regulatory requirements for any product prepared by a pharmacy.
I understand that the space is limited. The background should be a lighter color, and the pharmacist will hand write the information (with a darker color marker).
EXTERNAL USE
Pharmacy: Terma, 18 Blvd. Kr. Olvenov, Sofia 1327, ph. 02 4736159
Rx No. Date
Patient Name age
Pharmacist Good until:
Please, view it to scale of 4 cm in diameter (which is the actual label of the Face Cream Intense), so you will have a better feeling of the design.
Thank you so much.

```html
<!DOCTYPE html>
<html lang="en">
<head>
<meta charset="utf-8">
<title>Velo Skina – Eye Care Cream Labels</title>
<link href="https://fonts.googleapis.com/css2?family=Source+Sans+3:wght@400;600&display=swap" rel="stylesheet">
<style>
  :root {
    --backdrop: #c4c4c4;
    --lid-black: #060606;
    --lid-pattern: #111111;
    --gold: #d6b25e;
    --white: #ffffff;
    --base-cream: #f6f4f1;
    --base-pattern: #efebe7;
    --ink: #1a1a1a;
  }
  html, body {
    margin: 0;
    width: 1200px;
    height: 790px;
    overflow: hidden;
    background: var(--backdrop);
    font-family: "Source Sans 3", Arial, sans-serif;
  }
  .label {
    position: absolute;
    top: 192px;
    width: 357px;
    height: 357px;
  }
  .label--lid { left: 243px; }
  .label--base { left: 624px; }
  .label text { font-family: "Source Sans 3", Arial, sans-serif; }
  .lid-motto { fill: var(--white); font-size: 16px; letter-spacing: 3px; }
  .brand-name { fill: var(--gold); font-size: 30px; }
  .product-name { fill: var(--white); font-size: 24px; }
  .product-variant { fill: var(--white); font-size: 20px; letter-spacing: 2px; }
  .product-series { fill: var(--gold); font-size: 19px; }
  .ingredients { fill: var(--white); font-size: 12.5px; }
  .base-title { fill: var(--ink); font-size: 24px; }
  .pharmacy-info { fill: var(--ink); font-size: 19px; }
  .field-label { fill: var(--ink); font-size: 16px; font-weight: 600; }
  .sign-label { fill: var(--ink); font-size: 18px; }
</style>
</head>
<body>

<svg class="label label--lid" viewBox="0 0 446 446" aria-label="Upper lid label">
  <defs>
    <linearGradient id="silverRing" x1="0" y1="0" x2="1" y2="1">
      <stop offset="0" stop-color="#6f6f6f"/>
      <stop offset="0.35" stop-color="#f2f2f2"/>
      <stop offset="0.6" stop-color="#8a8a8a"/>
      <stop offset="1" stop-color="#e6e6e6"/>
    </linearGradient>
    <path id="mottoPath" d="M 20,223 A 203 203 0 1 1 426,223 A 203 203 0 1 1 20,223"/>
  </defs>
  <circle cx="223" cy="223" r="223" fill="var(--lid-black)"/>
  <circle cx="223" cy="223" r="186" fill="var(--lid-pattern)" role="img" aria-label="Subtle dark damask background pattern"/>
  <circle cx="223" cy="223" r="187" fill="none" stroke="url(#silverRing)" stroke-width="3"/>
  <text class="lid-motto">
    <textPath href="#mottoPath" startOffset="12" textLength="1190" lengthAdjust="spacing">Handmade . Doctor formulated . Registered Pharmacy . Highest Ethical Standards .</textPath>
  </text>

  <text class="brand-name" x="223" y="114" text-anchor="middle">velo skina</text>
  <text class="product-name" x="223" y="165" text-anchor="middle">EYE CARE CREAM</text>
  <text class="product-variant" x="223" y="193" text-anchor="middle">intensive</text>
  <text class="product-series" x="223" y="230" text-anchor="middle">Doctor Series</text>
  <line x1="62" y1="242" x2="384" y2="242" stroke="var(--gold)" stroke-width="2.5"/>

  <text class="ingredients" text-anchor="middle">
    <tspan x="223" y="273">Ingredients: Marigold extract, Witch Hazel Distillate,</tspan>
    <tspan x="223" y="289">Water, Glycerin, Stearyl Alcohol, Wheat Germ Oil,</tspan>
    <tspan x="223" y="305">Polysorbate60, Sesame Oil, MyristylMyristate, Cetyl</tspan>
    <tspan x="223" y="321">Alcohol, Sorbitan Stearate, Phenoxyethanol, Calendula</tspan>
    <tspan x="223" y="337">Extract, Cornflower Extract, Sodium Alginate, Sodium</tspan>
    <tspan x="223" y="353">Citrate, Mica, Vit. C, Vit. E.</tspan>
  </text>
</svg>

<svg class="label label--base" viewBox="0 0 446 446" aria-label="Bottom pharmacy label">
  <circle cx="223" cy="223" r="223" fill="var(--base-cream)" role="img" aria-label="Light cream damask background pattern"/>
  <circle cx="223" cy="223" r="190" fill="none" stroke="var(--gold)" stroke-width="4" stroke-dasharray="8 5"/>
  <circle cx="223" cy="223" r="183" fill="none" stroke="var(--gold)" stroke-width="2"/>

  <text class="base-title" x="223" y="92" text-anchor="middle">EXTERNAL USE</text>
  <text class="pharmacy-info" text-anchor="middle">
    <tspan x="223" y="138">Pharmacy: Terma, 18 Blvd. Kr.</tspan>
    <tspan x="223" y="158">Olvenov, Sofia 1327</tspan>
    <tspan x="223" y="182">ph. 02 4736159</tspan>
  </text>

  <rect x="75" y="203" width="297" height="37" fill="var(--white)" stroke="var(--ink)" stroke-width="2"/>
  <text class="field-label" x="81" y="227">Rx No:</text>
  <text class="field-label" x="250" y="227">Date:</text>

  <rect x="75" y="254" width="297" height="37" fill="var(--white)" stroke="var(--ink)" stroke-width="2"/>
  <text class="field-label" x="81" y="278">For:</text>
  <text class="field-label" x="250" y="278">Age:</text>

  <text class="sign-label" x="95" y="324">Good Until:</text>
  <line x1="193" y1="326" x2="342" y2="326" stroke="var(--ink)" stroke-width="1"/>
  <text class="sign-label" x="95" y="352">Pharmacist:</text>
  <line x1="195" y1="354" x2="344" y2="354" stroke="var(--ink)" stroke-width="1"/>
</svg>

</body>
</html>
```